Blueberry Road side sign

I want a sign to put on the side of the road to advertise the that I have fresh local blueberries for sale. attatched is my company logo.
I want to use the same font that is used in my logo design.
I want "blueberries" written across the sign,
with maybe a couple of berries after the writing.

```html
<!DOCTYPE html>
<html lang="en">
<head>
<meta charset="utf-8">
<title>Blueberries Roadside Sign</title>
<link href="https://fonts.googleapis.com/css2?family=Pacifico&family=Tinos:ital,wght@1,700&display=swap" rel="stylesheet">
<style>
  :root {
    --page-bg: #ffffff;
    --berry-blue: #0f54a4;
    --tagline-blue: #1757a6;
    --sign-top: #545456;
    --sign-mid: #c9c9cb;
    --sign-bottom: #ffffff;
    --sign-edge: #1a1a1a;
    --fruit-dark: #2e3550;
    --fruit-mid: #5b6690;
    --leaf: #3f9a3c;
  }
  html, body {
    margin: 0;
    padding: 0;
    width: 1200px;
    height: 1000px;
    overflow: hidden;
    background: var(--page-bg);
  }
  .canvas {
    position: relative;
    width: 1200px;
    height: 1000px;
  }
  .sign {
    position: absolute;
    left: 77px;
    top: 246px;
    width: 1042px;
    height: 521px;
    border: 1px solid var(--sign-edge);
    background: linear-gradient(to bottom, var(--sign-top) 0%, var(--sign-mid) 30%, #f1f1f2 58%, var(--sign-bottom) 100%);
    overflow: hidden;
  }
  .headline {
    position: absolute;
    left: 104px;
    top: 118px;
    margin: 0;
    font-family: "Pacifico", cursive;
    font-weight: 400;
    font-size: 112px;
    line-height: 1;
    color: var(--berry-blue);
    white-space: nowrap;
  }
  .berry-cluster {
    position: absolute;
    left: 718px;
    top: 178px;
    width: 212px;
    height: 168px;
  }
  .brand {
    position: absolute;
    left: 46px;
    top: 408px;
    display: flex;
    align-items: center;
    gap: 16px;
  }
  .brand-dot {
    width: 70px;
    height: 70px;
    border-radius: 50%;
    background: var(--berry-blue);
  }
  .brand-name {
    font-family: "Pacifico", cursive;
    font-size: 40px;
    line-height: 1;
    color: var(--berry-blue);
    white-space: nowrap;
  }
  .tagline {
    position: absolute;
    left: 602px;
    top: 452px;
    margin: 0;
    font-family: "Tinos", "Times New Roman", serif;
    font-style: italic;
    font-weight: 700;
    font-size: 25px;
    line-height: 1;
    color: var(--tagline-blue);
    white-space: nowrap;
  }
</style>
</head>
<body>
<div class="canvas">
  <section class="sign">
    <h1 class="headline">Blueberries</h1>

    <svg class="berry-cluster" viewBox="0 0 212 168" role="img" aria-label="Photo of three fresh blueberries with green leaves">
      <defs>
        <radialGradient id="fruitTone" cx="45%" cy="40%" r="60%">
          <stop offset="0%" stop-color="var(--fruit-mid)"/>
          <stop offset="100%" stop-color="var(--fruit-dark)"/>
        </radialGradient>
      </defs>
      <ellipse cx="106" cy="84" rx="104" ry="80" fill="url(#fruitTone)" opacity="0.9"/>
    </svg>

    <div class="brand">
      <span class="brand-dot"></span>
      <span class="brand-name">Bramble Bay</span>
    </div>

    <p class="tagline">FRESH LOCAL BLUEBERRIES</p>
  </section>
</div>
</body>
</html>
```